Business Card Ayurvedic Massage

I'm starting with my ayurvedic massage business and need a business card design. The design should be inline with my brand/logo as well as with the design of my website (www.lumo-thara.ch).
Front: logo and text "Ayurvedische Massagen"
back: name and adress (see details https://www.lumo-thara.ch/kontakt.html)

```html
<!DOCTYPE html>
<html lang="de">
<head>
<meta charset="utf-8">
<title>lumo-thara – Visitenkarte</title>
<link href="https://fonts.googleapis.com/css2?family=PT+Sans:wght@400;700&display=swap" rel="stylesheet">
<style>
  :root{
    --bg:#2b2b2b;
    --red:#8c0a0c;
    --red-deep:#7a0709;
    --red-pattern:#9a1416;
    --gold:#d9a43a;
    --gold-dark:#b07a22;
    --white:#ffffff;
  }
  *{box-sizing:border-box;margin:0;padding:0}
  html,body{width:1200px;height:892px;overflow:hidden;background:var(--bg);
    font-family:"PT Sans",sans-serif}
  .stage{position:relative;width:1200px;height:892px}
  .card{position:absolute;width:560px;height:320px;overflow:hidden;
    box-shadow:0 14px 30px rgba(0,0,0,.55)}

  /* Front */
  .card--front{left:90px;top:70px;background:var(--red)}
  .card--front .pattern{position:absolute;inset:0;
    background:radial-gradient(circle at 50% 50%,var(--red-pattern),var(--red-deep))}
  .brand-name{position:absolute;left:0;right:0;top:112px;text-align:center;
    color:var(--gold);font-weight:700;font-size:44px;line-height:1.1;letter-spacing:1px}
  .brand-tagline{position:absolute;left:0;right:0;top:176px;text-align:center;
    color:var(--gold);font-size:16px;letter-spacing:2px}
  .brand-url{position:absolute;left:0;right:0;top:232px;text-align:center;
    color:var(--gold);font-size:15px;letter-spacing:6px}

  /* Back */
  .card--back{left:550px;top:480px;background:var(--white)}
  .card--back svg.bands{position:absolute;inset:0}
  .person{position:absolute;left:36px;top:44px;color:var(--white)}
  .person-name{font-weight:700;font-size:24px;line-height:1}
  .person-role{font-size:15px;letter-spacing:.5px}
  .contact{position:absolute;left:36px;top:170px;color:var(--white);
    font-size:15px;line-height:20px}
  .contact .note{font-size:11px}
  .contact-row{display:flex;align-items:center;gap:10px}
  .contact-row svg{width:13px;height:13px;flex:none}
  .logo-area{position:absolute;left:350px;top:104px;width:190px;height:70px}
  .logo-art{position:absolute;width:44px;height:56px;top:6px;border-radius:4px;
    background:linear-gradient(180deg,var(--gold),var(--red))}
  .logo-art--left{left:0}
  .logo-art--right{right:0}
  .logo-name{position:absolute;left:48px;right:48px;top:24px;text-align:center;
    color:var(--red);font-weight:700;font-size:17px}
</style>
</head>
<body>
<main class="stage">

  <section class="card card--front" aria-label="Vorderseite">
    <div class="pattern" role="img" aria-label="Rotes Ornamentmuster im Hintergrund"></div>
    <p class="brand-name">lumo-thara</p>
    <p class="brand-tagline">Ayurvedische Massagen</p>
    <p class="brand-url">WWW.LUMO-THARA.CH</p>
  </section>

  <section class="card card--back" aria-label="Rückseite">
    <svg class="bands" viewBox="0 0 560 320" preserveAspectRatio="none" aria-hidden="true">
      <path d="M0 0 H300 C330 110 380 230 470 320 H0 Z" fill="var(--gold)"/>
      <path d="M0 0 H292 C322 110 372 230 458 320 H0 Z" fill="var(--white)"/>
      <path d="M0 0 H284 C314 112 362 232 446 320 H0 Z" fill="var(--gold-dark)"/>
      <path d="M0 0 H270 C300 114 346 234 426 320 H0 Z" fill="var(--red)"/>
    </svg>

    <div class="person">
      <p class="person-name">MARA LIND</p>
      <p class="person-role">PRESIDENT</p>
    </div>

    <div class="contact">
      <p>Ilse Vormann, lumo-thara</p>
      <p>Birkenweg 14</p>
      <p>8712 Talbach (SZ)</p>
      <p class="contact-row">
        <svg viewBox="0 0 16 16" aria-hidden="true"><path fill="var(--white)" d="M3 1l3 3-2 2c1 2 3 4 5 5l2-2 3 3-2 3C7 14 2 9 1 3z"/></svg>
        <span>+41 70 000 12 34 <span class="note">(Bitte keine Werbung)</span></span>
      </p>
      <p class="contact-row">
        <svg viewBox="0 0 16 16" aria-hidden="true"><rect x="1" y="3" width="14" height="10" fill="var(--white)"/><path d="M1 3l7 6 7-6" stroke="var(--red)" fill="none"/></svg>
        <span>info@lumo-thara.ch</span>
      </p>
      <p class="contact-row">
        <svg viewBox="0 0 16 16" aria-hidden="true"><circle cx="8" cy="8" r="7" fill="var(--white)"/><path d="M5 8h6M8 5l3 3-3 3" stroke="var(--red)" stroke-width="1.5" fill="none"/></svg>
        <span>www.lumo-thara.ch</span>
      </p>
    </div>

    <div class="logo-area">
      <div class="logo-art logo-art--left" role="img" aria-label="Geschmückter Elefant, links"></div>
      <p class="logo-name">lumo-thara</p>
      <div class="logo-art logo-art--right" role="img" aria-label="Geschmückter Elefant, rechts"></div>
    </div>
  </section>

</main>
</body>
</html>
```